Family Office for small businesses needs clear web site

I founded VORUSK Family Office, which is a french family office design to change the relationship between the customer and the wealth manager/insurance broker.
The main focus is : we give back to the client all the commissions / hidden costs we gain from the insurance companies / real estate builders and we bill to the client an annual fee proportional to the wealth. Thus a transparent relationship exempt from conflict of interest

I want a WORPRESS theme design that will be easily customizable in the future. Using and existing wordpress theme is not a problem, as long as i get to customize it in the future if necessary.
I want the web site to be Simple, clear, explaining the concepts detailed in the word doc i join to this project
In the chart are some of the things we do (not all, but most).
Also i joined some question a client might ask himself before calling us

i am available to clarify any issue or concepts

Reason: I want to let new designer submit their proposal. I really wish to conclude this design contest to move forward on other projects.

Target Market(s)

small businesses, specically their boss

Industry/Entity Type

Office

Number of Pages Required

1 page

Font styles to use
Serif

Colors
85acd3
3176b5
0455a3
cedeed
eaf1f7
cee9f5
85cae6
33a6d7
0692cd

Requirements
Must have
• I would like to have a one page wordpress theme personalized by a designer.
• I don't really care if you use an existing wordpress theme, as long as it can be upgraded/customized later on using wordpress/admin.
• I can even provide some themes I bought if it can help maintain the budget..
• O I can pay additional fee for a theme you bought to provide the design..

```html
<!DOCTYPE html>
<html lang="en">
<head>
<meta charset="utf-8">
<title>VORUSK Family Office</title>
<link href="https://fonts.googleapis.com/css2?family=Open+Sans:wght@300;400;600;700&family=Raleway:wght@400;500;600;700&display=swap" rel="stylesheet">
<style>
:root{
  --blue:#0692cd;
  --blue-deep:#0455a3;
  --blue-mid:#3176b5;
  --blue-soft:#85acd3;
  --blue-pale:#eaf1f7;
  --blue-sky:#33a6d7;
  --ink:#333b44;
  --muted:#7b838c;
  --grey-bg:#f2f4f6;
  --dark:#1f2226;
  --darker:#17191c;
  --white:#ffffff;
}
*{box-sizing:border-box;margin:0;padding:0}
html,body{width:1200px;height:3028px;overflow:hidden}
body{font-family:"Open Sans",Arial,sans-serif;color:var(--ink);background:var(--white);font-size:13px;line-height:1.6}
h1,h2,h3,h4{font-family:"Raleway","Open Sans",sans-serif;font-weight:600}
.wrap{width:1040px;margin:0 auto;position:relative}

/* header */
.site-header{height:80px;background:var(--white);border-bottom:1px solid #e3e6ea}
.site-header .wrap{display:flex;align-items:center;justify-content:space-between;height:80px}
.brand-name{font-family:"Raleway",sans-serif;font-size:22px;font-weight:600;color:var(--blue-mid);line-height:1;letter-spacing:.5px}
.main-nav{display:flex;gap:4px}
.main-nav a{font-size:11px;font-weight:600;color:#555;text-decoration:none;padding:8px 14px;letter-spacing:.5px}
.main-nav a.is-active{color:var(--blue)}

/* hero */
.hero{height:560px;position:relative;overflow:hidden;
  background:linear-gradient(180deg,#6f7b85 0%,#8f9aa2 35%,#7e8a7a 62%,#4f6b3a 82%,#3e5a2c 100%)}
.hero-photo{position:absolute;inset:0}
.hero-text{position:absolute;left:0;right:0;top:180px;text-align:center;color:var(--white)}
.hero-kicker{font-size:16px;font-weight:400;letter-spacing:.5px}
.hero-title{font-size:54px;font-weight:700;letter-spacing:2px;margin:6px 0 10px}
.hero-copy{width:640px;margin:0 auto;font-size:13px;opacity:.95}
.hero-dots{position:absolute;bottom:130px;left:0;right:0;display:flex;justify-content:center;gap:10px}
.hero-dots span{width:12px;height:12px;border-radius:50%;border:2px solid var(--white)}
.hero-dots span.on{background:var(--white)}
.hero-arrow{position:absolute;top:320px;color:var(--white);font-size:40px;line-height:1;opacity:.8}
.hero-arrow.left{left:24px}.hero-arrow.right{right:24px}

/* welcome */
.welcome{height:290px;background:var(--blue);color:var(--white);text-align:center;padding-top:70px}
.welcome h2{font-size:36px;letter-spacing:1px;font-weight:600}
.divider{display:flex;justify-content:center;align-items:center;gap:10px;margin:10px 0 22px}
.divider i{display:block;width:50px;height:1px;background:currentColor;opacity:.7}
.divider b{width:8px;height:8px;border-radius:50%;border:1px solid currentColor}
.welcome p{width:1000px;margin:0 auto;font-size:11px;line-height:1.75;opacity:.92}

/* services */
.services{height:510px;background:linear-gradient(90deg,var(--grey-bg) 0%,var(--grey-bg) 68%,#dfe3e8 100%);text-align:center;padding-top:70px;position:relative}
.services-photo{position:absolute;right:0;top:0;width:280px;height:100%;background:linear-gradient(90deg,rgba(242,244,246,0),#cfd5db)}
.services h2{font-size:38px;font-weight:500;color:#3a4048;position:relative}
.services .divider{color:var(--blue);margin:8px 0 6px}
.services-lead{font-size:13px;color:var(--muted);position:relative}
.service-cards{display:flex;justify-content:center;gap:32px;margin-top:64px;position:relative}
.service-card{width:312px;height:210px;background:var(--white);border:1px solid #dde2e7;position:relative;padding:66px 26px 0}
.service-icon{position:absolute;top:-38px;left:50%;margin-left:-38px;width:76px;height:76px;border-radius:50%;background:var(--blue);border:5px solid var(--white);display:flex;align-items:center;justify-content:center;box-shadow:0 0 0 1px #dde2e7}
.service-card h3{font-size:13px;font-weight:600;color:#3a4048;letter-spacing:.5px}
.service-card p{font-size:11px;color:var(--muted);margin:8px 0 14px}
.read-more{font-size:10px;font-weight:700;color:#3a4048;letter-spacing:.5px;text-decoration:none;border:1px solid #dde2e7;padding:4px 10px}

/* family office */
.family{height:480px;background:var(--white)}
.family .wrap{display:flex;align-items:center;height:480px;gap:60px}
.family-visual{width:440px;height:330px;border-radius:18px;background:#2a2d31;padding:20px 26px;flex:none}
.family-visual div{width:100%;height:100%;background:linear-gradient(135deg,#f4f7fa,#dbe6f0)}
.family-text{width:520px}
.family-text .eyebrow{font-size:18px;font-weight:600;color:var(--blue);font-family:"Raleway",sans-serif;margin:0;line-height:1.3}
.family-text h2{font-size:28px;font-weight:600;color:#2e343b;margin:2px 0 14px;letter-spacing:.5px;white-space:nowrap}
.family-text p{font-size:12px;color:var(--muted);margin-bottom:12px}
.tick-list{list-style:none}
.tick-list li{font-size:12px;color:var(--ink);display:flex;align-items:center;gap:8px;line-height:2}
.tick-list svg{flex:none}

/* approach */
.approach{height:400px;background:linear-gradient(90deg,#2c2f33 0%,#1c1e21 40%,#222427 100%);position:relative;color:var(--white);text-align:center;overflow:hidden}
.approach-photo{position:absolute;left:0;top:0;width:300px;height:100%;background:linear-gradient(90deg,#4a4e54,rgba(30,32,35,0))}
.approach-inner{position:relative;padding-top:56px}
.quote-mark{font-family:Georgia,serif;font-size:72px;line-height:.8;font-weight:700}
.approach h2{font-size:30px;font-weight:600;letter-spacing:1px;margin:10px 0 16px}
.approach p{width:840px;margin:0 auto;font-size:12px;opacity:.85}
.approach-nav{position:absolute;top:220px;font-size:26px;opacity:.8}
.approach-nav.left{left:170px}.approach-nav.right{right:170px}
.approach-dots{display:flex;justify-content:center;gap:8px;margin-top:30px}
.approach-dots span{width:12px;height:12px;border-radius:50%;background:#555}
.approach-dots span.on{background:var(--blue)}

/* news */
.news{height:440px;background:var(--white)}
.news .wrap{display:flex;gap:40px;padding-top:66px}
.news-intro{width:260px}
.news-intro h2{font-size:24px;font-weight:600;color:#2e343b;letter-spacing:.5px}
.news-intro h3{font-size:20px;font-weight:500;color:var(--blue);margin-bottom:14px}
.news-intro p{font-size:11px;color:var(--muted);margin-bottom:18px}
.btn{display:inline-block;background:var(--blue);color:var(--white);font-size:11px;font-weight:600;padding:8px 18px;text-decoration:none}
.news-cards{display:flex;gap:30px}
.news-card{width:220px}
.news-thumb{height:160px;margin-bottom:14px}
.news-card h4{font-size:14px;font-weight:500;color:#2e343b}
.news-card p{font-size:11px;color:var(--muted);margin:4px 0 8px}
.news-card a{font-size:10px;color:var(--blue);text-decoration:none;font-weight:600}

/* footer */
.site-footer{height:230px;background:var(--dark);color:#c7cbd0}
.site-footer .wrap{display:flex;gap:40px;padding-top:36px}
.foot-col h4{font-size:14px;font-weight:600;color:var(--white);letter-spacing:1px;margin-bottom:12px}
.foot-col p,.foot-col li{font-size:11px;line-height:1.7}
.foot-col ul{list-style:none}
.col-news{width:250px}.col-letter{width:300px}.col-info{width:180px}.col-contact{width:190px}
.foot-col .news-date{color:var(--white);font-weight:600;font-size:15px;margin:6px 0}
.socials{display:flex;gap:6px}
.socials span{width:20px;height:20px;border-radius:50%;background:#6f757c}
.letter-form{display:flex;margin-top:10px}
.letter-form span{width:200px;height:30px;background:var(--white)}
.letter-form b{background:var(--blue);color:var(--white);font-size:11px;padding:6px 16px}
.contact-line{display:flex;gap:8px;align-items:center}
.foot-bar{height:38px;background:var(--blue);color:var(--white);font-size:10px;text-align:center;line-height:38px}
</style>
</head>
<body>

<header class="site-header">
  <div class="wrap">
    <div class="brand"><span class="brand-name">VORUSK Family Office</span></div>
    <nav class="main-nav">
      <a class="is-active" href="#">HOME</a>
      <a href="#">ABOUT US</a>
      <a href="#">OUR SERVICE</a>
      <a href="#">OUR ADDED VALUE</a>
      <a href="#">TESTIMONIALS</a>
      <a href="#">CONTACT US</a>
    </nav>
  </div>
</header>

<section class="hero">
  <div class="hero-photo" role="img" aria-label="Row of trees with money-leaf crowns on green grass under a grey sky"></div>
  <span class="hero-arrow left">‹</span>
  <span class="hero-arrow right">›</span>
  <div class="hero-text">
    <p class="hero-kicker">Wealth MANAGEMENT Consultancy</p>
    <h1 class="hero-title">VORUSK STRATEGIES</h1>
    <p class="hero-copy">Nulla quis lorem ut libero malesuada feugiat. Curabitur non nulla sit amet nisl tempus convallis quis ac lectus. Curabitur arcu erat, accumsan id imperdiet et, porttitor at sem.</p>
  </div>
  <div class="hero-dots"><span class="on"></span><span></span><span></span></div>
</section>

<section class="welcome">
  <h2>WELCOME TO VORUSK</h2>
  <div class="divider"><i></i><b></b><i></i></div>
  <p>Sed ut perspiciatis unde omnis iste natus error sit voluptatem accusantium doloremque laudantium, totam rem aperiam, eaque ipsa quae ab illo inventore veritatis et quasi architecto beatae vitae dicta sunt explicabo. Nemo enim ipsam voluptatem quia voluptas sit aspernatur aut odit aut fugit, sed quia consequuntur magni dolores eos qui ratione voluptatem sequi nesciunt. Neque porro quisquam est, qui dolorem ipsum quia dolor sit amet, consectetur, adipisci velit, sed quia non numquam eius modi tempora incidunt ut labore et dolore magnam aliquam quaerat voluptatem. Ut enim ad minima veniam, quis nostrum exercitationem ullam corporis suscipit laboriosam.</p>
</section>

<section class="services">
  <div class="services-photo" role="img" aria-label="Faded photo of a business person holding a tablet"></div>
  <h2>OUR SERVICE OFFER</h2>
  <div class="divider"><i></i><b></b><i></i></div>
  <p class="services-lead">We see our business as a consulting activity foremost, which operates in compliance</p>
  <div class="service-cards">
    <article class="service-card">
      <div class="service-icon"><svg width="30" height="30" viewBox="0 0 30 30" fill="none" stroke="#fff" stroke-width="2"><circle cx="15" cy="12" r="7"/><path d="M12 20h6M12 24h6"/></svg></div>
      <h3>STRATEGIC CONSULTING</h3>
      <p>Lorem ipsum dolor sit amet, consectetur adipiscing elit. Fusce ultrices nisi ac facilisis, sed tempor magna luctus.</p>
      <a class="read-more" href="#">READ MORE ›</a>
    </article>
    <article class="service-card">
      <div class="service-icon"><svg width="30" height="30" viewBox="0 0 30 30" fill="none" stroke="#fff" stroke-width="2"><path d="M5 12h5l10-6v18l-10-6H5z"/><path d="M9 18l2 6"/></svg></div>
      <h3>OPERATIONAL ADVICE</h3>
      <p>Lorem ipsum dolor sit amet, consectetur adipiscing elit. Fusce ultrices nisi ac facilisis, sed tempor magna luctus.</p>
      <a class="read-more" href="#">READ MORE ›</a>
    </article>
    <article class="service-card">
      <div class="service-icon"><svg width="32" height="30" viewBox="0 0 32 30" fill="#fff"><circle cx="16" cy="9" r="5"/><circle cx="7" cy="12" r="3.5"/><circle cx="25" cy="12" r="3.5"/><path d="M8 26c0-6 4-9 8-9s8 3 8 9z"/><path d="M1 25c0-4 3-7 6-7 1 0 2 .3 2.5.6C8 20 7 22 7 25z"/><path d="M31 25c0-4-3-7-6-7-1 0-2 .3-2.5.6C24 20 25 22 25 25z"/></svg></div>
      <h3>THE FAMILY COUNSELING</h3>
      <p>Lorem ipsum dolor sit amet, consectetur adipiscing elit. Fusce ultrices nisi ac facilisis, sed tempor magna luctus.</p>
      <a class="read-more" href="#">READ MORE ›</a>
    </article>
  </div>
</section>

<section class="family">
  <div class="wrap">
    <div class="family-visual"><div role="img" aria-label="Tablet screen showing an organisation chart of family office services"></div></div>
    <div class="family-text">
      <p class="eyebrow">FAMILY OFFICE</p>
      <h2>VORUSK IS A FAMILY OFFICE</h2>
      <p>A Family Office is a consultancy wealth management firm that acts in your interest only.</p>
      <p>VORUSK offer the range of services under the family office:</p>
      <ul class="tick-list">
        <li><svg width="12" height="12" viewBox="0 0 12 12"><circle cx="6" cy="6" r="6" fill="#0692cd"/><path d="M3 6l2 2 4-4" stroke="#fff" stroke-width="1.5" fill="none"/></svg>Consulting In Financial Investments</li>
        <li><svg width="12" height="12" viewBox="0 0 12 12"><circle cx="6" cy="6" r="6" fill="#0692cd"/><path d="M3 6l2 2 4-4" stroke="#fff" stroke-width="1.5" fill="none"/></svg>Insurance Brokerage</li>
        <li><svg width="12" height="12" viewBox="0 0 12 12"><circle cx="6" cy="6" r="6" fill="#0692cd"/><path d="M3 6l2 2 4-4" stroke="#fff" stroke-width="1.5" fill="none"/></svg>Advising On Real Estate And Unlisted Companies</li>
        <li><svg width="12" height="12" viewBox="0 0 12 12"><circle cx="6" cy="6" r="6" fill="#0692cd"/><path d="M3 6l2 2 4-4" stroke="#fff" stroke-width="1.5" fill="none"/></svg>Legal And Tax Support</li>
        <li><svg width="12" height="12" viewBox="0 0 12 12"><circle cx="6" cy="6" r="6" fill="#0692cd"/><path d="M3 6l2 2 4-4" stroke="#fff" stroke-width="1.5" fill="none"/></svg>Administrative And Budgetary Support</li>
      </ul>
    </div>
  </div>
</section>

<section class="approach">
  <div class="approach-photo" role="img" aria-label="Business man in a suit standing by a window"></div>
  <span class="approach-nav left">‹</span>
  <span class="approach-nav right">›</span>
  <div class="approach-inner">
    <div class="quote-mark">“</div>
    <h2>THE APPROACH IS RIGOROUS</h2>
    <p>Lorem ipsum dolor sit amet, consectetur adipiscing elit, sed do eiusmod tempor incididunt ut labore et dolore magna aliqua. Ut enim ad minim veniam, quis nostrud exercitation ullamco laboris nisi ut aliquip ex ea commodo consequat. Duis aute irure dolor in reprehenderit in voluptate velit esse cillum dolore eu fugiat nulla pariatur. Excepteur sint occaecat cupidatat non proident.</p>
    <div class="approach-dots"><span class="on"></span><span></span><span></span></div>
  </div>
</section>

<section class="news">
  <div class="wrap">
    <div class="news-intro">
      <h2>GET TO KNOW MORE</h2>
      <h3>News and Events</h3>
      <p>Nam libero tempore, cum soluta nobis est eligendi optio cumque nihil impedit quo minus id quod maxime placeat facere possimus, omnis voluptas assumenda est, omnis dolor repellendus temporibus autem.</p>
      <a class="btn" href="#">READ MORE</a>
    </div>
    <div class="news-cards">
      <article class="news-card">
        <div class="news-thumb" role="img" aria-label="Young plant growing from a stack of coins" style="background:linear-gradient(135deg,#dfe9c8,#8fb25a)"></div>
        <h4>Duis aute irure dolor</h4>
        <p>Lorem ipsum dolor sit amet, consectetur adipiscing elit sed do eiusmod.</p>
        <a href="#">Read more ›</a>
      </article>
      <article class="news-card">
        <div class="news-thumb" role="img" aria-label="Modern city office buildings against a blue sky" style="background:linear-gradient(180deg,#b9cfe3,#7d8d9c)"></div>
        <h4>Duis aute irure dolor</h4>
        <p>Lorem ipsum dolor sit amet, consectetur adipiscing elit sed do eiusmod.</p>
        <a href="#">Read more ›</a>
      </article>
      <article class="news-card">
        <div class="news-thumb" role="img" aria-label="Advisor meeting a couple at a desk" style="background:linear-gradient(135deg,#f1ede8,#c9b7a6)"></div>
        <h4>Duis aute irure dolor</h4>
        <p>Lorem ipsum dolor sit amet, consectetur adipiscing elit sed do eiusmod.</p>
        <a href="#">Read more ›</a>
      </article>
    </div>
  </div>
</section>

<footer>
  <div class="site-footer">
    <div class="wrap">
      <div class="foot-col col-news">
        <h4>LATEST NEWS</h4>
        <p>Lorem ipsum dolor sit amet, consectetur adipiscing elit, sed do eiusmod tempor.</p>
        <p class="news-date">Oct 15, 2015</p>
        <div class="socials"><span></span><span></span><span></span><span></span></div>
      </div>
      <div class="foot-col col-letter">
        <h4>JOIN OUR NEWSLETTER</h4>
        <p>Excepteur sint occaecat cupidatat non proident, sunt in culpa.</p>
        <div class="letter-form"><span></span><b>SUBSCRIBE</b></div>
      </div>
      <div class="foot-col col-info">
        <h4>INFORMATION</h4>
        <ul><li>HOME</li><li>ABOUT US</li><li>OUR ADDED VALUE</li><li>OUR SERVICE</li><li>CONTACT US</li></ul>
      </div>
      <div class="foot-col col-contact">
        <h4>CONTACT US</h4>
        <p>VORUSK Family Office<br>14 rue des Lilas, Paris</p>
        <p class="contact-line"><svg width="12" height="12" viewBox="0 0 12 12" fill="#c7cbd0"><path d="M2 1h3l1 3-2 1a7 7 0 003 3l1-2 3 1v3c-6 1-10-3-9-9z"/></svg>+33 1 84 27 55 90</p>
        <p class="contact-line"><svg width="12" height="10" viewBox="0 0 12 10" fill="none" stroke="#c7cbd0"><rect x=".5" y=".5" width="11" height="9"/><path d="M.5 .5l5.5 5 5.5-5"/></svg>contact@vorusk-office.example</p>
      </div>
    </div>
  </div>
  <div class="foot-bar">Copyright © 2015 VORUSK Family Office. All Rights Reserved.</div>
</footer>

</body>
</html>
```